Landing Page & Logo for Over 50s Guaranteed Life Cover

www.silveryearsquote.com provides a method of comparing guaranteed life cover for consumers aged over 50. The approach we are initially looking to deploy is a simple landing page that provides the user with high level information about Silver Years Quote and allows them to see which provider is offering the best deal by ranking providers in a table. This will compare costs / core features in the same way as shown in the attached file.

The page should incorporate a new logo design for SilverYearsQuote.com which should be similar in design to the website goldenagepolicies.com.

Key elements of the landing page include:

Header (incorporating new logo and strapline e.g. "helping you find the best cover at the best price")
Introductory Text (to allow brief description of the service)
Comparison Table (to show top 10 providers - to include logos)
Table Links (allows customer to link directly from the table to the providers site)
Helpline (details of helpline number 0800 731 2946 - not actual number)
Join The Club (allows customers to sign up - using their email - to the over 50s club for more information and offers)

Other design elements welcomed to ensure the landing page is simple to understand, easy to navigate, visually appealing, focused on driving action / sales.
Updates

Additional payment approx. £60 for incorporating a new logo. Added Monday, April 25, 2016

Target Market(s)

50 - 80

Industry/Entity Type

Insurance

Logo Text

silveryearsquote and strapline "helping you find the best cover at the best price"

Number of Pages Required

1 page

Font styles to use
Sans Serif

Colors
a5ce39
add136
cadf82
eaf2ce
ffffff

Requirements
Nice to have
• Ideally created so content can be managed via WordPress.

```html
<!DOCTYPE html>
<html lang="en">
<head>
<meta charset="utf-8">
<title>SilverYearsQuote – Comparing Guaranteed Life Cover</title>
<link href="https://fonts.googleapis.com/css2?family=Montserrat:wght@600;700&family=Raleway:wght@300;400;500;600&family=Cormorant+Garamond:ital,wght@1,500&display=swap" rel="stylesheet">
<style>
:root{
  --green:#a5ce39;
  --green-2:#add136;
  --row-dark:#c5dd7c;
  --row-light:#eaf2ce;
  --club:#dbe9ae;
  --orange:#fb4b12;
  --ink:#333;
  --white:#fff;
}
*{box-sizing:border-box;margin:0;padding:0}
html,body{width:954px;height:1200px;overflow:hidden}
body{font-family:'Raleway',sans-serif;color:var(--ink);background:var(--white);position:relative}
.site-header{height:63px;background:var(--green);display:flex;align-items:center;justify-content:space-between;padding:0 70px}
.brand{font-family:'Montserrat',sans-serif;font-weight:700;font-size:19px;color:var(--white);letter-spacing:.5px}
.strapline{font-family:'Cormorant Garamond',serif;font-style:italic;font-size:19px;color:var(--white)}
.hero{position:absolute;top:63px;left:0;width:954px;height:445px;overflow:hidden}
.hero-photo{position:absolute;inset:0;background:linear-gradient(100deg,#c9c9c7 0%,#d8cfc6 35%,#c9a890 58%,#b58f79 75%,#8f8c88 100%)}
.hero-shade{position:absolute;inset:0;background:linear-gradient(90deg,rgba(0,0,0,.18),rgba(0,0,0,0) 60%)}
.hero-copy{position:absolute;left:69px;top:98px;color:var(--white)}
.hero-copy h1{font-family:'Montserrat',sans-serif;font-weight:600;font-size:29px;line-height:35px}
.hero-copy p{font-weight:300;font-size:13.5px;line-height:23px;margin-top:10px;width:390px}
.cta{display:inline-block;margin-top:15px;background:var(--orange);color:var(--white);font-size:14px;padding:0 21px;height:41px;line-height:41px;border:1px solid #fff3}
.slide-arrow{position:absolute;top:242px;width:38px;height:38px;border-radius:50%;background:rgba(255,255,255,.2)}
.slide-arrow.prev{left:11px}.slide-arrow.next{left:903px}
.helpline{position:absolute;left:293px;top:358px;width:369px;height:44px;display:flex;align-items:center;justify-content:center;gap:10px;z-index:2}
.helpline svg.tab{position:absolute;inset:0;z-index:-1}
.helpline .label{font-size:19px;color:#444}
.helpline .number{font-family:'Montserrat',sans-serif;font-size:22px;color:var(--orange);font-weight:600;letter-spacing:.5px}
.compare{position:absolute;left:69px;top:402px;width:816px;border-collapse:collapse;font-size:10.5px;z-index:2}
.compare th{background:var(--green);color:var(--white);font-weight:500;height:40px;font-size:10.5px;border-right:1px solid #c4e07a}
.compare td{height:51px;text-align:center;border-right:1px solid var(--white)}
.compare tr:nth-child(odd) td{background:var(--row-light)}
.compare tr:nth-child(even) td{background:var(--row-dark)}
.provider{display:flex;align-items:center;justify-content:center;gap:5px;font-weight:600;font-size:12px;color:#1f3b66}
.provider i{width:9px;height:9px;background:var(--orange);display:block}
.actions{display:flex;flex-direction:column;align-items:center;gap:5px}
.btn{display:block;width:57px;height:15px;line-height:15px;font-size:8px;color:var(--white)}
.btn.buy{background:var(--orange)}.btn.info{background:var(--green)}
.club{position:absolute;top:989px;left:0;width:954px;height:150px;background:linear-gradient(120deg,#e4efc0,#d6e6a2 50%,#e2edbc);text-align:center}
.club h2{font-weight:400;font-size:22px;margin-top:24px;color:#444}
.club p{font-size:13px;margin-top:6px;color:#444}
.signup{display:flex;justify-content:center;margin-top:13px}
.signup span{width:248px;height:32px;background:var(--white);text-align:left;padding-left:11px;line-height:32px;font-size:12px;color:#888;border:1px solid #e6e6e6}
.signup b{width:96px;height:32px;background:var(--orange);color:var(--white);line-height:32px;font-size:13px;font-weight:700}
.site-footer{position:absolute;top:1139px;left:0;width:954px;height:61px;background:var(--green);display:flex;align-items:center;justify-content:space-between;padding:0 69px;color:var(--white);font-size:10.5px}
.social{display:flex;align-items:center;gap:8px}
.social i{width:25px;height:25px;border:1.5px solid var(--white);border-radius:50%;display:block}
.social span{margin-right:8px}
</style>
</head>
<body>
<header class="site-header">
  <div class="brand">SILVERYEARSQUOTE</div>
  <div class="strapline">Helping you find the best cover at the best Price</div>
</header>

<section class="hero">
  <div class="hero-photo" role="img" aria-label="Photo of a smiling older man with his daughter and grandson"></div>
  <div class="hero-shade"></div>
  <div class="hero-copy">
    <h1>Comparing Guaranteed<br>Life Cover</h1>
    <p>SilverYearsQuote has teamed up with our friends at Quotara to bring you high quality low cost cover from leading insurers.</p>
    <span class="cta">GET A FREE QUOTES</span>
  </div>
  <svg class="slide-arrow prev" viewBox="0 0 38 38"><path d="M22 10 L14 19 L22 28" fill="none" stroke="#fff" stroke-width="1.5"/></svg>
  <svg class="slide-arrow next" viewBox="0 0 38 38"><path d="M16 10 L24 19 L16 28" fill="none" stroke="#fff" stroke-width="1.5"/></svg>
</section>

<div class="helpline">
  <svg class="tab" viewBox="0 0 369 44" preserveAspectRatio="none"><path d="M0 0 H369 L355 44 H14 Z" fill="#fff"/></svg>
  <svg width="28" height="28" viewBox="0 0 28 28"><circle cx="14" cy="14" r="12.5" fill="none" stroke="#444" stroke-width="1.6"/><path d="M10 8 L12 8 L13 11 L11.5 12.5 Q13 16 15.5 16.5 L17 15 L20 16 L20 18 Q19 20 16 19.5 Q10 17 8.5 11 Q8.5 8.5 10 8 Z" fill="#444"/></svg>
  <span class="label">Helpline</span>
  <span class="number">0800 731 2946</span>
</div>

<table class="compare">
  <colgroup><col style="width:111px"><col style="width:98px"><col style="width:75px"><col style="width:98px"><col style="width:98px"><col style="width:85px"><col style="width:54px"><col style="width:54px"><col style="width:54px"><col style="width:89px"></colgroup>
  <thead><tr><th>Company Name</th><th>Cover Amount</th><th>Premium</th><th>Payment Term</th><th>Total Payment</th><th>Initial Period</th><th>Rank</th><th>Start</th><th>End</th><th>Buy Now</th></tr></thead>
  <tbody>
    <tr><td><span class="provider"><i></i>Meadowfield</span></td><td>$4,200</td><td>$10.00</td><td>40 years</td><td>$4,800.00</td><td>24 months</td><td>1</td><td>yes</td><td>yes</td><td><span class="actions"><span class="btn buy">Buy Now »</span><span class="btn info">More Info »</span></span></td></tr>
    <tr><td><span class="provider"><i></i>Orvana</span></td><td>$3,700</td><td>$10.00</td><td>20 years</td><td>$4,500.00</td><td>12 months</td><td>2</td><td>yes</td><td>yes</td><td><span class="actions"><span class="btn buy">Buy Now »</span><span class="btn info">More Info »</span></span></td></tr>
    <tr><td><span class="provider"><i></i>Hearthstone</span></td><td>$5,200</td><td>$10.00</td><td>40 years</td><td>$7,800.00</td><td>16 months</td><td>3</td><td>yes</td><td>yes</td><td><span class="actions"><span class="btn buy">Buy Now »</span><span class="btn info">More Info »</span></span></td></tr>
    <tr><td><span class="provider"><i></i>Talbridge</span></td><td>$7,700</td><td>$10.00</td><td>20 years</td><td>$9,800.00</td><td>12 months</td><td>4</td><td>yes</td><td>yes</td><td><span class="actions"><span class="btn buy">Buy Now »</span><span class="btn info">More Info »</span></span></td></tr>
    <tr><td><span class="provider"><i></i>Corvell</span></td><td>$3,500</td><td>$10.00</td><td>40 years</td><td>$4,800.00</td><td>16 months</td><td>5</td><td>yes</td><td>yes</td><td><span class="actions"><span class="btn buy">Buy Now »</span><span class="btn info">More Info »</span></span></td></tr>
    <tr><td><span class="provider"><i></i>Brookvale</span></td><td>$6,700</td><td>$10.00</td><td>20 years</td><td>$7,800.00</td><td>12 months</td><td>6</td><td>yes</td><td>yes</td><td><span class="actions"><span class="btn buy">Buy Now »</span><span class="btn info">More Info »</span></span></td></tr>
    <tr><td><span class="provider"><i></i>Sheltera</span></td><td>$3,500</td><td>$10.00</td><td>40 years</td><td>$4,800.00</td><td>16 months</td><td>7</td><td>yes</td><td>yes</td><td><span class="actions"><span class="btn buy">Buy Now »</span><span class="btn info">More Info »</span></span></td></tr>
    <tr><td><span class="provider"><i></i>Norcrest</span></td><td>$6,700</td><td>$10.00</td><td>20 years</td><td>$7,800.00</td><td>12 months</td><td>8</td><td>yes</td><td>yes</td><td><span class="actions"><span class="btn buy">Buy Now »</span><span class="btn info">More Info »</span></span></td></tr>
    <tr><td><span class="provider"><i></i>Brand</span></td><td>$3,500</td><td>$10.00</td><td>40 years</td><td>$4,800.00</td><td>16 months</td><td>9</td><td>yes</td><td>yes</td><td><span class="actions"><span class="btn buy">Buy Now »</span><span class="btn info">More Info »</span></span></td></tr>
    <tr><td><span class="provider"><i></i>Ashgrove</span></td><td>$6,700</td><td>$10.00</td><td>20 years</td><td>$7,800.00</td><td>12 months</td><td>10</td><td>yes</td><td>yes</td><td><span class="actions"><span class="btn buy">Buy Now »</span><span class="btn info">More Info »</span></span></td></tr>
  </tbody>
</table>

<section class="club">
  <h2>Join The Club</h2>
  <p>Over 50s club for more information and Offers</p>
  <div class="signup"><span>Email address</span><b>SIGN UP</b></div>
</section>

<footer class="site-footer">
  <span>Copyrights © 2016 Silver Years Quote. All rights reserved.</span>
  <div class="social"><span>Connected Us On:</span><i></i><i></i><i></i><i></i></div>
</footer>
</body>
</html>
```